Clear sticker design for packaging

I need 4” diameter clear stickers designed for birthdays, thank you , teachers day and all the other special days to complete my gift packaging. They will go on the top of each tube to differentiate each gift for each occasion. Our design is on craft paper and I’ve uploaded a few examples of what we are trying to achieve. Last picture is the top of our tube where the stickers will be placed. We don’t want too much color unless for Christmas and Valentine’s Day maybe! We are working with black and gold or a mixture of both mostly

```html
<!DOCTYPE html>
<html lang="en">
<head>
<meta charset="utf-8">
<title>Occasion Stickers</title>
<link href="https://fonts.googleapis.com/css2?family=Dancing+Script:wght@600;700&family=Montserrat:wght@600&family=Bungee+Inline&family=Libre+Baskerville&display=swap" rel="stylesheet">
<style>
  :root {
    --kraft: #d7b582;
    --kraft-light: #dfc08f;
    --kraft-dark: #cfa96f;
    --ink: #111111;
    --outline: #2a2218;
    --holly: #3f8f3c;
    --holly-leaf: #5aa543;
    --berry: #c8232c;
    --valentine-red: #e3232e;
    --gold-1: #f7ec8a;
    --gold-2: #e9b82a;
    --gold-3: #c98f12;
  }
  * { margin: 0; padding: 0; box-sizing: border-box; }
  html, body { width: 1200px; height: 1200px; overflow: hidden; }
  body {
    background:
      radial-gradient(circle at 30% 20%, var(--kraft-light), transparent 60%),
      radial-gradient(circle at 75% 80%, var(--kraft-dark), transparent 55%),
      var(--kraft);
  }
  .sheet { position: relative; width: 1200px; height: 1200px; }
  .sticker { position: absolute; width: 348px; height: 348px; }
  .sticker svg { width: 348px; height: 348px; overflow: visible; }
  .cut-line { fill: none; stroke: var(--outline); stroke-width: 0.8; }
  .sans-caps { font-family: 'Montserrat', sans-serif; font-weight: 600; fill: var(--ink); letter-spacing: 1.5px; }
  .script { font-family: 'Dancing Script', cursive; font-weight: 700; fill: var(--ink); }
  .display-inline { font-family: 'Bungee Inline', sans-serif; fill: var(--ink); }
  .serif-arc { font-family: 'Libre Baskerville', serif; fill: var(--valentine-red); }
  .sticker--christmas { left: 201px; top: 58px; }
  .sticker--valentine { left: 650px; top: 58px; }
  .sticker--father-black { left: 201px; top: 431px; }
  .sticker--father-gold { left: 650px; top: 431px; }
  .sticker--mother-black { left: 201px; top: 795px; }
  .sticker--mother-gold { left: 638px; top: 795px; }
</style>
</head>
<body>
<main class="sheet">
  <svg width="0" height="0" style="position:absolute">
    <defs>
      <linearGradient id="gold" x1="0" y1="0" x2="1" y2="1">
        <stop offset="0" stop-color="var(--gold-1)"/>
        <stop offset="0.55" stop-color="var(--gold-2)"/>
        <stop offset="1" stop-color="var(--gold-3)"/>
      </linearGradient>
    </defs>
  </svg>

  <!-- Christmas -->
  <div class="sticker sticker--christmas">
    <svg viewBox="0 0 348 348">
      <circle class="cut-line" cx="174" cy="174" r="173"/>
      <circle cx="174" cy="172" r="121" fill="none" stroke="var(--holly)" stroke-width="1.6"/>
      <rect role="img" aria-label="Holly leaves with red poinsettia" x="96" y="36" width="156" height="56" rx="28" fill="var(--holly-leaf)"/>
      <rect role="img" aria-label="Holly leaves with red baubles" x="98" y="258" width="148" height="56" rx="28" fill="var(--holly-leaf)"/>
      <text class="sans-caps" x="174" y="136" font-size="28" text-anchor="middle">MERRY</text>
      <text class="script" x="174" y="222" font-size="84" text-anchor="middle" textLength="298" lengthAdjust="spacingAndGlyphs">Christmas</text>
    </svg>
  </div>

  <!-- Valentine -->
  <div class="sticker sticker--valentine">
    <svg viewBox="0 0 348 348">
      <defs>
        <path id="valentine-arc" d="M44 164 A132 132 0 0 1 304 164"/>
      </defs>
      <circle class="cut-line" cx="174" cy="174" r="173"/>
      <text class="serif-arc" font-size="32"><textPath href="#valentine-arc" startOffset="50%" text-anchor="middle">Happy Valentines</textPath></text>
      <path d="M174 270 C120 225 69 190 69 150 C69 122 90 108 112 108 C140 108 160 122 174 142 C188 122 208 108 236 108 C260 108 279 124 279 152 C279 192 228 225 174 270 Z" fill="url(#gold)"/>
      <text class="script" x="180" y="202" font-size="74" text-anchor="middle">Love</text>
      <path d="M66 216 C90 300 250 312 286 216" fill="none" stroke="var(--valentine-red)" stroke-width="2.4"/>
      <rect role="img" aria-label="Red leafy branch" x="40" y="200" width="34" height="118" rx="17" transform="rotate(-28 57 259)" fill="var(--valentine-red)"/>
      <rect role="img" aria-label="Red leafy branch" x="276" y="200" width="34" height="118" rx="17" transform="rotate(28 293 259)" fill="var(--valentine-red)"/>
    </svg>
  </div>

  <!-- Father's Day black -->
  <div class="sticker sticker--father-black">
    <svg viewBox="0 0 348 348">
      <circle class="cut-line" cx="174" cy="174" r="173"/>
      <text class="script" x="174" y="96" font-size="56" text-anchor="middle">Happy</text>
      <text class="display-inline" x="174" y="174" font-size="54" text-anchor="middle" textLength="290" lengthAdjust="spacingAndGlyphs">FATHER'S</text>
      <text class="display-inline" x="174" y="234" font-size="54" text-anchor="middle" textLength="118" lengthAdjust="spacingAndGlyphs">DAY</text>
      <rect role="img" aria-label="Black moustache" x="83" y="250" width="184" height="46" rx="23" fill="var(--ink)"/>
    </svg>
  </div>

  <!-- Father's Day gold -->
  <div class="sticker sticker--father-gold">
    <svg viewBox="0 0 348 348">
      <circle class="cut-line" cx="174" cy="174" r="173"/>
      <text class="script" x="174" y="98" font-size="56" text-anchor="middle">Happy</text>
      <text class="display-inline" x="174" y="176" font-size="54" text-anchor="middle" textLength="290" lengthAdjust="spacingAndGlyphs">FATHER'S</text>
      <text class="display-inline" x="174" y="236" font-size="54" text-anchor="middle" textLength="118" lengthAdjust="spacingAndGlyphs">DAY</text>
      <rect role="img" aria-label="Gold moustache" x="76" y="252" width="196" height="46" rx="23" fill="url(#gold)" stroke="var(--ink)" stroke-width="1.2"/>
    </svg>
  </div>

  <!-- Mother's Day black -->
  <div class="sticker sticker--mother-black">
    <svg viewBox="0 0 348 348">
      <circle class="cut-line" cx="174" cy="174" r="173"/>
      <circle cx="174" cy="174" r="158" fill="none" stroke="var(--ink)" stroke-width="1.6"/>
      <circle cx="176" cy="172" r="151" fill="none" stroke="var(--ink)" stroke-width="1.2"/>
      <circle cx="172" cy="176" r="146" fill="none" stroke="var(--ink)" stroke-width="1"/>
      <text class="sans-caps" x="174" y="116" font-size="28" text-anchor="middle">HAPPY</text>
      <text class="script" x="178" y="208" font-size="78" text-anchor="middle" textLength="254" lengthAdjust="spacingAndGlyphs">Mother's</text>
      <text class="sans-caps" x="174" y="254" font-size="28" text-anchor="middle">DAY</text>
    </svg>
  </div>

  <!-- Mother's Day gold -->
  <div class="sticker sticker--mother-gold">
    <svg viewBox="0 0 348 348">
      <circle class="cut-line" cx="174" cy="174" r="173"/>
      <circle cx="174" cy="174" r="158" fill="none" stroke="var(--ink)" stroke-width="1.6"/>
      <circle cx="176" cy="172" r="151" fill="none" stroke="var(--ink)" stroke-width="1.2"/>
      <circle cx="172" cy="176" r="146" fill="none" stroke="var(--ink)" stroke-width="1"/>
      <text class="sans-caps" x="174" y="116" font-size="28" text-anchor="middle">HAPPY</text>
      <text class="script" x="178" y="208" font-size="78" text-anchor="middle" textLength="254" lengthAdjust="spacingAndGlyphs" fill="url(#gold)" stroke="var(--ink)" stroke-width="1.2" style="fill:url(#gold)">Mother's</text>
      <text class="sans-caps" x="174" y="254" font-size="28" text-anchor="middle">DAY</text>
    </svg>
  </div>
</main>
</body>
</html>
```